I would like an amazing design for a eCommerce website called trailhaven.net.

The logo was designed on SketchHive and is attached below. Whatever your design - it MUST use this logo. Please don't waste your time designing new logos.

The logo is on both black and white backgrounds as I've not yet made my mind up whether to ditch "cool black" in favour of more "fresh, clean white"! I'd like to look at both options.

Trail Haven is going to be the first destination of choice for anyone who is bored or frustrated at home and wants a life full of adventure. It will stock outdoor clothing and equipment, training kit, expedition gear, and travel clothing and accessories.

But it is a very cool place to go. A fun and exciting Aladdin's cave full of fantastic adventure kit. We will stock inflatable pack rafts, machetes, hammocks and other expedition gear as well as standard outdoor clothing.

This is NOT a geeky outdoor store selling pac-a-macs and walking poles.

The unique thing is that everything stocked is hand selected by me, Tom Bexley, an experienced explorer who became the first person to walk the Amazon in 2010. tombexley.net is my site. I now make TV for Horizon Network.

There will be items at every price level from "only the best" - absolute top end kit, to "get the job done" - stuff that won't break the bank. Everything stocked works. If it doesn't - I won't sell it.

So although the theme is fun and adventurous I have to have it also feeling like a place of professional, expert advice. A place of substance and depth.

Thanks in advance for all your ideas and designs!

Best
Tom
Updates

The designs that I like the best have used jungle images as background wallpaper - possible with a green tint to them so that they really do look like background rather than the focus. The focus should obviously be the kit for sale. The best designs have this on a fresh white or light grey background so that it stands out. I like the main logo being in a black header and footer. But the feel of the site can easily become too dark if too much back is used or if the green background image is too dark. We want adventure and cool - but it has to feel light and professional enough to be accessible by people of all ages. Most websites that are successful are white after all and whilst I'd like to be a bit more adventurous than that we shouldn't over do the darkness!

I'm not really a massive fan of side bars and would hope that whichever site I chose had a mega menu system like Corwin Latch that could navigate quickly and easily to any item intuitively.

Any sliders must be about selling kit not images of me.

Thanks so much to everyone who has submitted designs - there are some VERY cool ones out there at the moment

Best,
Tom

Target Market(s)

The target market is primarily 16 to 50 years old outdoor enthusiasts however I will be selling to older people and kids, male and female, so it can't be too modern, too macho, or too complicated to put anyone off.

Requirements
Must have
• Bold, professional, adventurous feel. Not cluttered but not so minimalist that it looks boring too. I would like to select a few colours and work with them.
• Red for high lighted emphasis. See logo
• Greens/blacks/greys as background.
• Clean menu system. I'm probably going use a tailored version of http://plumtide-theme.shopsample.net with mega menus.
Nice to have
• Some personalisation that makes the site mine. Use of hi res images below as background could work although I am keen for the site to look clean and easy to navigate.
Should not have
• Hundreds of boxes and text and clutter. I want this site to show off the items in a classy manner. This is NOT gear barn.net! This is a site where hand selected items are proudly displayed and put together, after a lot of thought.

```html
<!DOCTYPE html>
<html lang="en">
<head>
<meta charset="utf-8">
<title>Trail Haven – Outdoor Adventure Kit</title>
<link rel="stylesheet" href="https://fonts.googleapis.com/css2?family=Oswald:wght@300;400;500;700&family=Roboto:wght@400;700&display=swap">
<style>
:root{
  --red:#cc1f26;
  --price-red:#d10a0a;
  --black:#000;
  --header:#1d1d1d;
  --panel:#1a1a1a;
  --card-grey:#5a5a5a;
  --btn:#333;
  --footer:#e9e9e9;
  --text-dark:#333;
  --white:#fff;
}
*{margin:0;padding:0;box-sizing:border-box}
html,body{width:938px;height:1200px;overflow:hidden}
body{position:relative;background:var(--black);font-family:Roboto,Arial,sans-serif;color:var(--white)}
.abs{position:absolute}

.topbar{left:0;top:21px;width:938px;height:39px;background:var(--red);font-size:12px}
.topbar .welcome{left:29px;top:13px}
.topbar .account{left:650px;top:13px;display:flex;align-items:center;gap:8px}
.topbar .cart{left:760px;top:13px;display:flex;align-items:center;gap:7px}
.topbar .sep{top:0;width:1px;height:39px;background:rgba(0,0,0,.25)}
.topbar .social{left:846px;top:14px;display:flex;gap:7px}
.topbar .social i{display:block;width:12px;height:12px;border-radius:50%;background:var(--white)}

.header{left:0;top:60px;width:938px;height:118px;background:var(--header)}
.logo{left:11px;top:4px;width:422px;height:97px;background:#161616;padding:24px 0 0 14px}
.logo .name{font-family:Oswald,sans-serif;font-weight:700;font-size:34px;color:var(--red);letter-spacing:2px;line-height:1}
.logo .tag{font-family:Oswald,sans-serif;font-weight:300;font-size:16px;color:var(--white);margin-top:6px;letter-spacing:.5px}
.phone{right:29px;top:18px;display:flex;align-items:center;gap:8px;font-family:Oswald,sans-serif;font-weight:300;font-size:31px}
.search{left:653px;top:60px;width:218px;height:34px;background:var(--white);color:#888;font-size:13px;padding:10px 11px}
.search-btn{left:871px;top:60px;width:40px;height:34px;background:var(--red);display:flex;align-items:center;justify-content:center}

.hero-photo{left:15px;top:199px;width:621px;height:329px;background:linear-gradient(135deg,#5f7a4a 0%,#8aa36a 35%,#b9c2b4 55%,#6a5548 80%,#3d4a32 100%)}
.hero-panel{left:636px;top:199px;width:285px;height:329px;background:var(--panel);padding:34px 0 0 22px;font-family:Oswald,sans-serif}
.hero-panel .l1{font-weight:300;font-size:36px;line-height:1}
.hero-panel .l2{font-weight:700;font-size:52px;line-height:1;margin-top:2px}
.hero-panel .l3{font-weight:300;font-size:30px;line-height:1.1}
.hero-panel .l3 em{font-style:normal;color:var(--red)}
.hero-panel .copy{font-weight:300;font-size:17px;line-height:20px;margin-top:16px;width:240px}
.hero-panel .cta{font-weight:500;font-size:25px;margin-top:18px;margin-left:-3px}

.card{top:553px;width:205px;height:369px}
.card .media{height:233px;background:var(--white);position:relative}
.card .media .ph{position:absolute;left:20px;top:12px;width:165px;height:170px}
.card .add{position:absolute;left:7px;bottom:0;height:28px;padding:0 11px;background:var(--btn);font-size:12px;line-height:28px}
.card .price{height:38px;background:var(--price-red);display:flex;align-items:center;justify-content:space-between;padding:0 8px 0 10px}
.card .now{font-family:Oswald,sans-serif;font-weight:500;font-size:26px}
.card .was{font-family:Oswald,sans-serif;font-weight:500;font-size:14px;text-decoration:line-through}
.card .info{height:98px;background:var(--card-grey);padding:24px 9px 0}
.card .info h3{font-size:13px;font-weight:700}
.card .info p{font-size:11px;line-height:13px;color:#d6d6d6;margin-top:8px}

.footer-rule{left:0;top:969px;width:938px;height:6px;background:var(--red)}
.footer{left:0;top:975px;width:938px;height:225px;background:var(--footer);color:var(--text-dark)}
.footer h4{font-family:Oswald,sans-serif;font-weight:500;font-size:25px;color:var(--red);letter-spacing:-.3px}
.footer ul{list-style:none;margin-top:8px;font-size:12px;font-weight:700;line-height:17px}
.footer .col{top:30px}
.footer .follow li{display:flex;align-items:center;gap:8px;margin-bottom:4px}
.footer .follow i{display:block;width:16px;height:16px;border-radius:50%;background:var(--btn)}
.footer .addr{font-size:12px;line-height:14px;margin-top:12px}
.footer .tel{display:flex;align-items:center;gap:7px;margin-top:6px;font-family:Oswald,sans-serif;font-weight:300;font-size:26px}
.footer .legal{left:0;top:180px;width:938px;border-top:1px solid #9a9a9a;padding:14px 0 0 21px;font-size:12px;font-weight:700}
</style>
</head>
<body>

<div class="topbar abs">
  <span class="welcome abs">Welcome to Trail Haven</span>
  <span class="account abs">
    <svg width="17" height="17" viewBox="0 0 17 17"><circle cx="8.5" cy="5" r="4" fill="#fff"/><path d="M1 17c0-5 3-7 7.5-7S16 12 16 17z" fill="#fff"/></svg>my account</span>
  <span class="sep abs" style="left:747px"></span>
  <span class="cart abs">
    <svg width="19" height="16" viewBox="0 0 19 16"><path d="M0 1h3l3 9h10l2-7H5" fill="none" stroke="#fff" stroke-width="2"/><circle cx="7" cy="14" r="1.6" fill="#fff"/><circle cx="15" cy="14" r="1.6" fill="#fff"/></svg>0 items</span>
  <span class="sep abs" style="left:835px"></span>
  <span class="social abs"><i></i><i></i><i></i><i></i></span>
</div>

<div class="header abs">
  <div class="logo abs">
    <div class="name">TRAIL HAVEN</div>
    <div class="tag">Everything for a life of adventure - by Tom Bexley</div>
  </div>
  <div class="phone abs">
    <svg width="28" height="28" viewBox="0 0 28 28"><circle cx="14" cy="14" r="12.5" fill="none" stroke="#fff" stroke-width="2"/><path d="M9 8c1-1 2-1 3 1l1 2c0 1-1 2-1 2 1 2 2 3 4 4 0 0 1-1 2-1l2 1c2 1 2 2 1 3-2 2-5 1-8-2s-5-7-4-10z" fill="#fff"/></svg>
    1(800) 555-0147
  </div>
  <div class="search abs">Search store...</div>
  <div class="search-btn abs">
    <svg width="24" height="22" viewBox="0 0 24 22"><circle cx="8" cy="8" r="6" fill="none" stroke="#fff" stroke-width="3"/><path d="M12.5 12.5l8 7" stroke="#fff" stroke-width="4" stroke-linecap="round"/></svg>
  </div>
</div>

<div class="hero-photo abs" role="img" aria-label="Family of hikers with backpacks waving in a pine forest"></div>
<div class="hero-panel abs">
  <div class="l1">NEED</div>
  <div class="l2">EQUIPMENT</div>
  <div class="l3">FOR FULL <em>ADVENTURE?</em></div>
  <div class="copy">We are very cool place to go. A fun and exciting Aladdin's cave full of fantastic adventure kit.</div>
  <div class="cta">SHOP NOW!</div>
</div>

<div class="card abs" style="left:15px">
  <div class="media"><div class="ph" role="img" aria-label="Red and black camera backpack" style="background:radial-gradient(circle,#b8242a 0%,#2a2a2a 60%,#fff 72%)"></div><span class="add">add to cart</span></div>
  <div class="price"><span class="now">$199.00</span><span class="was">$250.00</span></div>
  <div class="info"><h3>Lorem ipsum dolor sit am ...</h3><p>Consectetuer adipiscing elit, sed diam nonummy nibh euismod tincidunt ...</p></div>
</div>
<div class="card abs" style="left:249px">
  <div class="media"><div class="ph" role="img" aria-label="Green rope hammock" style="background:radial-gradient(ellipse 60% 25%,#5f6b5a 0%,#9aa596 60%,#fff 100%)"></div><span class="add">add to cart</span></div>
  <div class="price"><span class="now">$245.00</span><span class="was">$500.00</span></div>
  <div class="info"><h3>Magna aliquam erat volutpat</h3><p>Ut wisi enim ad minim veniam, quis nostrud exerci tation ullamcorper ...</p></div>
</div>
<div class="card abs" style="left:482px">
  <div class="media"><div class="ph" role="img" aria-label="Black and yellow inflatable pack raft" style="background:radial-gradient(ellipse 55% 30%,#222 0%,#3a3a2a 60%,#fff 100%)"></div><span class="add">add to cart</span></div>
  <div class="price"><span class="now">$955.00</span><span class="was">$1200.00</span></div>
  <div class="info"><h3>Duis autem vel eum iriure ...</h3><p>Feugiat nulla facilisis at vero eros et accumsan et iusto odio dignissim ...</p></div>
</div>
<div class="card abs" style="left:716px">
  <div class="media"><div class="ph" role="img" aria-label="Machete with sheath" style="background:linear-gradient(135deg,#fff 20%,#cfcfcf 45%,#222 55%,#8a5a3a 70%,#fff 80%)"></div><span class="add">add to cart</span></div>
  <div class="price"><span class="now">$69.50</span><span class="was">$200.00</span></div>
  <div class="info"><h3>Nam liber tempor cum solu ...</h3><p>Typi non habent claritatem insitam; est usus legentis in iis qui facit eo...</p></div>
</div>

<div class="footer-rule abs"></div>
<div class="footer abs">
  <div class="col abs" style="left:24px">
    <h4>NAVIGATION</h4>
    <ul><li>Home</li><li>Catalog</li><li>Blog</li><li>About Us</li><li>Contact Us</li></ul>
  </div>
  <div class="col abs" style="left:260px">
    <h4>MY ACCOUNT</h4>
    <ul><li>My Account</li><li>My Cart</li><li>Login</li></ul>
  </div>
  <div class="col abs follow" style="left:498px">
    <h4>FOLLOW US</h4>
    <ul><li><i></i>Chirper</li><li><i></i>Facepage</li><li><i></i>Circles +</li><li><i></i>Linkwork</li></ul>
  </div>
  <div class="col abs" style="left:729px">
    <h4>CONTACT US</h4>
    <p class="addr">48 Cedar Ridge Lane Suite 12<br>Millbrook, Vermont 05401</p>
    <div class="tel">
      <svg width="26" height="26" viewBox="0 0 28 28"><circle cx="14" cy="14" r="12.5" fill="none" stroke="#333" stroke-width="2"/><path d="M9 8c1-1 2-1 3 1l1 2c0 1-1 2-1 2 1 2 2 3 4 4 0 0 1-1 2-1l2 1c2 1 2 2 1 3-2 2-5 1-8-2s-5-7-4-10z" fill="#333"/></svg>
      0-44-5550192
    </div>
  </div>
  <div class="legal abs">© Copyright Trail Haven 2014. All Rights Reserved.</div>
</div>

</body>
</html>
```